agricultural technology company needs business cards*

design a business card that represents our business well. please see our website: vastrelbyfieldseal.com.au
professional, simple, clean lines, not complicated or floral.....

```html
<!DOCTYPE html>
<html lang="en">
<head>
<meta charset="utf-8">
<title>Vastrelby FieldSeal – Business Cards</title>
<link href="https://fonts.googleapis.com/css2?family=Archivo:wght@700&family=Josefin+Sans:wght@300;400&display=swap" rel="stylesheet">
<style>
  :root {
    --navy: #22315b;
    --green: #2f9f48;
    --lime: #98bd3c;
    --paper: #ffffff;
    --backdrop: #e8e8e6;
    --ink-light: #d9dde8;
  }
  html, body {
    margin: 0;
    width: 1200px;
    height: 801px;
    overflow: hidden;
    background: var(--backdrop);
  }
  .sheet {
    position: relative;
    width: 1200px;
    height: 801px;
    display: flex;
    align-items: center;
    justify-content: center;
    gap: 40px;
  }
  .card {
    position: relative;
    width: 560px;
    height: 320px;
    background: var(--paper);
    box-shadow: 0 6px 18px rgba(0,0,0,0.12);
    overflow: hidden;
  }
  .card-shapes {
    position: absolute;
    inset: 0;
  }
  .wordmark {
    position: absolute;
    font-family: "Archivo", Arial, sans-serif;
    font-weight: 700;
    line-height: 0.92;
    letter-spacing: -0.5px;
    margin: 0;
  }
  .card-front .wordmark {
    left: 28px;
    top: 34px;
    font-size: 40px;
    color: var(--green);
  }
  .card-back .wordmark {
    left: 34px;
    bottom: 34px;
    font-size: 52px;
    color: var(--paper);
  }
  .contact-person {
    position: absolute;
    left: 34px;
    top: 180px;
    font-family: "Josefin Sans", sans-serif;
  }
  .person-name {
    margin: 0;
    font-size: 22px;
    font-weight: 400;
    color: var(--green);
  }
  .person-role {
    margin: 2px 0 12px;
    font-size: 14px;
    font-weight: 300;
    color: var(--ink-light);
  }
  .contact-list {
    list-style: none;
    margin: 0;
    padding: 0;
    font-size: 13px;
    font-weight: 300;
    color: var(--ink-light);
  }
  .contact-list li {
    display: flex;
    align-items: center;
    gap: 8px;
    margin-bottom: 4px;
  }
  .contact-list .web { font-weight: 400; color: var(--paper); }
  .contact-icon { width: 14px; height: 14px; flex: none; }
  .address {
    position: absolute;
    right: 40px;
    top: 112px;
    margin: 0;
    font-family: "Josefin Sans", sans-serif;
    font-style: normal;
    font-weight: 300;
    font-size: 14px;
    line-height: 1.4;
    color: var(--ink-light);
    text-align: left;
  }
</style>
</head>
<body>
<main class="sheet">

  <section class="card card-front" aria-label="Business card front">
    <svg class="card-shapes" viewBox="0 0 560 320" aria-hidden="true">
      <polygon points="0,184 500,62 560,62 560,292 0,292" fill="var(--navy)"/>
      <polygon points="420,50 560,16 560,38 500,50" fill="var(--green)"/>
    </svg>
    <h1 class="wordmark">Vastrelby<br>FieldSeal</h1>
    <div class="contact-person">
      <p class="person-name">Maren Oduya</p>
      <p class="person-role">Founder &amp; Co-Owner</p>
      <ul class="contact-list">
        <li>
          <svg class="contact-icon" viewBox="0 0 14 14"><circle cx="7" cy="7" r="7" fill="var(--green)"/><path d="M4.6 3.8l1.3 1.3-.7.9c.5 1 1.2 1.7 2.2 2.2l.9-.7 1.3 1.3-.8 1c-2.6-.6-4.6-2.6-5.2-5.2z" fill="var(--navy)"/></svg>
          <span>1300 482 316</span>
        </li>
        <li>
          <svg class="contact-icon" viewBox="0 0 14 14"><circle cx="7" cy="7" r="7" fill="var(--green)"/><rect x="3.5" y="4.5" width="7" height="5" fill="none" stroke="var(--navy)" stroke-width="1"/><path d="M3.5 4.5L7 7.3l3.5-2.8" fill="none" stroke="var(--navy)" stroke-width="1"/></svg>
          <span>info@vastrelbyfieldseal.com.au</span>
        </li>
        <li>
          <svg class="contact-icon" viewBox="0 0 14 14"><circle cx="7" cy="7" r="7" fill="var(--green)"/><circle cx="7" cy="7" r="3.6" fill="none" stroke="var(--navy)" stroke-width="1"/><path d="M3.4 7h7.2M7 3.4c-1.6 2-1.6 5.2 0 7.2M7 3.4c1.6 2 1.6 5.2 0 7.2" fill="none" stroke="var(--navy)" stroke-width="0.9"/></svg>
          <span class="web">vastrelbyfieldseal.com.au</span>
        </li>
      </ul>
    </div>
    <address class="address">14 Harlow Rd,<br>Kelmscott WA 6111</address>
  </section>

  <section class="card card-back" aria-label="Business card back">
    <svg class="card-shapes" viewBox="0 0 560 320" aria-hidden="true">
      <polygon points="0,28 130,28 560,150 560,320 0,320" fill="var(--navy)"/>
    </svg>
    <p class="wordmark">Vastrelby<br>FieldSeal</p>
  </section>

</main>
</body>
</html>
```